serious, thorough, light and simple - that's my advice and mediations

My business card should combine my logo (uploaded file) and my homepage (https://fellor-mediation.webnestsite.com).

Contact Information for Business Card

Name: Sabine Fellor di Vanti
Phone: 076 412 58 94
mail: sfellor@postkiv.ch
web: www.fellor-di-vanti.ch

```html
<!DOCTYPE html>
<html lang="de">
<head>
<meta charset="utf-8">
<title>Sabine Fellor di Vanti – Visitenkarte</title>
<link rel="stylesheet" href="https://fonts.googleapis.com/css2?family=Open+Sans:wght@300;400&display=swap">
<style>
  :root {
    --paper: #ffffff;
    --ink: #1a1a1a;
    --brand-gold: #a8844e;
    --brand-green: #1f6b4a;
  }
  html, body {
    margin: 0;
    padding: 0;
    overflow: hidden;
    background: var(--paper);
  }
  .card {
    position: relative;
    width: 1200px;
    height: 777px;
    background: var(--paper);
    font-family: "Open Sans", Arial, sans-serif;
    color: var(--ink);
    overflow: hidden;
  }
  .contact {
    position: absolute;
    left: 79px;
    top: 74px;
    margin: 0;
    font-weight: 300;
    font-size: 44px;
    line-height: 65px;
  }
  .contact-row { display: block; white-space: nowrap; }
  .contact-label { display: inline-block; margin-right: 24px; }
  .holder-name {
    position: absolute;
    left: 79px;
    top: 310px;
    margin: 0;
    font-weight: 400;
    font-size: 44px;
    line-height: 65px;
    white-space: nowrap;
  }
  .brand {
    position: absolute;
    right: 102px;
    top: 490px;
    display: flex;
    align-items: center;
    gap: 18px;
  }
  .brand-mark {
    display: block;
    width: 18px;
    height: 18px;
    background: var(--brand-green);
  }
  .brand-name {
    font-weight: 400;
    font-size: 52px;
    line-height: 70px;
    color: var(--brand-gold);
    white-space: nowrap;
  }
</style>
</head>
<body>
  <main class="card">
    <p class="contact">
      <span class="contact-row"><span class="contact-label">Phone</span>076 412 58 94</span>
      <span class="contact-row"><span class="contact-label">Mail</span>sfellor@postkiv.ch</span>
      <span class="contact-row"><span class="contact-label">Web</span>www.fellor-di-vanti.ch</span>
    </p>
    <p class="holder-name">Sabine Fellor di Vanti</p>
    <div class="brand">
      <span class="brand-mark" aria-hidden="true"></span>
      <span class="brand-name">Wege im Dialog</span>
    </div>
  </main>
</body>
</html>
```